Maren's Treasured Tunes - 2014

I need a CD cover and insert design for a CD that includes songs my daughter (Maren Dulack) has recorded. She is a 17 year old vocalist and uses accompaniment tracks as well as 2 songs with live accompaniment. The CD is dedicated to her mother and each song is dedicated to an individual. The CD is intended to be given as gifts to family and friends.

The CD is titled "2014"

There are 5 songs on the CD:

1. "Evening Lantern" (originally recorded by Paolo Vantreni and Lorette Fave). This is a duet with Maren and her father.
2. "Open Road" (Originally recorded by Copper Hollows). This is a duet Maren and her father.
3. "All That Your Mercy Holds" (originally recorded by Gloria Bastrelli) This is sung by Maren. Accompanied on keyboard by Tamsin Holgreve.
4. "Keep a Light On For Me" (originally sung by Vera Castlewood).
5. "Lean On Us" (originally sung by Dario Quell) sung by Maren accompanied on guitar by Tamsin Holgreve.

This is a mixture of songs that have special meaning to Maren. The CD should convey her fun, bubbly but mature personality. It should be colorful and fun not dark and harsh. She is a "Texas" girl but she isn't into country music. She loves anything "Texas".

With the dedications included for each song and the CD, there will need to be interior printing and background design that may include a foldout in order to fit everything.

CD Dedication:
"I dedicate this cd to my mom. Even though I don't show it all the time, I appreciate her and the unconditional love she shows me. Through everything that I do I want to make her proud. Thank you for always having hope and faith in me and providing a life for me that I am so blessed to live. I love you more an more every day"

Song Dedications:
"Evening Lantern"
As many people know, “Evening Lantern” has been our most requested song to sing. Growing up I had heard my dad sing this song with my aunt and I was so mesmerized by their performances and couldn’t wait to one day sing this song with my dad. My dad and I have been singing together since I was 4 but this song sparked a different kind of relationship and musical connection with him. It was challenging at first and he pushed me to work hard and to push myself to discover vocal capabilities that I didn’t know I had. I dedicate this song to my dad for always motivating me to be the best I can be not only musically but socially, academically and most of all spiritually. Dad, I love you more than words can say.

"Open Road"
I have never been a fan of country music let alone attempted to sing a country song but this song completely changed my perspective on it. My dad and I first sang this song at our Pastors retirement party celebrating he and his wife’s 23 year long dedication to our church and to recognize his love for country music. They became apart of our family in many ways and I am so blessed to call them family. This song is dedicated to Pastor Glen and Faye Durbin for everything fron putting up with my grandparents to sharing every Easter with us. I miss them so much but I know that they will forever be apart of our family no matter where God places them.

"All That Your Mercy Holds"
When first introduced to this song I hated it. When having to choose a song to sing I always went with a ballad because that was my comfort zone. So when asked to sing a gospel song I was very overwhelmed. I never fully understood why people would say that they are “in love with music” or “music was their passion”. I obviously enjoyed music but I had never felt that connection with it until the first time I performed this song. Every note, every word, every dynamic meant something to me and my passion for music was forever changed. I dedicate this song to Tamsin Holgreve for working with me hour upon hour to help me vocally improve and for teaching me that it’s okay to step outside the box and to not just be comfortable all the time.

"Keep a Light on for Me"
I heard this song for the first time and sang it 3 days later for my end of the year choir concert. My mom had been searching songs for me to sing and as soon as she introduced this song to me I fell in love with it. This song is typically meant to be sung about a romantic love but while performing this song I couldn’t help but think of my grandparents and how they are always watching over me. I dedicate this song to my guardian angels, my protectors, and the two people that I love and miss more than anything in this world Oma and Opa.

"Lean On Us"
When I first sang this song I was performing at my voice recital for school. I chose to sing this song because it was fun and sweet. In the past few months this song has become very real to me. Although God and family are top priorities in my life, friends are such a huge part of my life as well. In 6Th grade I started a friendship with someone that I never knew would make such a great impact on my life. She became someone that I looked up to and someone that I could truly call my best friend. I dedicate this song to Kaylee Brandt for always putting up with me and investing in not only my life but my family’s life. No matter where life takes us in the next year I will forever be thankful for her friendship.

Special thanks to:

My Momma
Marla Quince (voice coach)
Lulu Padgett (High School choir director)
Mark Ostrand
Grant Vossler (Producer)

IMG_9670 is for the cover and IMG_9672 is for the back.

Thanks,

Curtis Dulack (father)

```html
<!DOCTYPE html>
<html lang="en">
<head>
<meta charset="utf-8">
<title>Maren's Treasured Tunes - 2014 — CD insert</title>
<link rel="stylesheet" href="https://fonts.googleapis.com/css2?family=Courgette&family=Great+Vibes&display=swap">
<style>
  :root {
    --page: #ffffff;
    --band: #231f20;
    --panel: #7b0f52;
    --pink: #e8177f;
    --pink-soft: #f59ac4;
    --bloom: #c4145f;
    --text: #ffffff;
  }
  * { margin: 0; padding: 0; box-sizing: border-box; }
  html, body {
    width: 1200px; height: 870px; overflow: hidden;
    background: var(--page);
  }
  .canvas { position: relative; width: 1200px; height: 870px; }

  .spread {
    position: absolute; left: 40px; width: 1110px; height: 369px;
    background: var(--band); overflow: hidden;
  }
  .spread--outside { top: 41px; }
  .spread--inside { top: 451px; }

  .panel {
    position: absolute; top: 31px; width: 308px; height: 308px;
    background: var(--panel);
    font-family: "Courgette", cursive;
    color: var(--text);
    padding: 12px 14px 0 16px;
  }
  .panel--1 { left: 30px; }
  .panel--2 { left: 400px; }
  .panel--3 { left: 770px; }

  .floral {
    position: absolute; left: 0; right: 0; bottom: 0; height: 175px;
    background:
      radial-gradient(ellipse at 20% 85%, rgba(232,23,127,.55), transparent 55%),
      radial-gradient(ellipse at 55% 90%, rgba(196,20,95,.5), transparent 55%),
      radial-gradient(ellipse at 88% 80%, rgba(232,23,127,.5), transparent 55%),
      linear-gradient(to bottom, transparent, rgba(232,23,127,.18));
    z-index: 1; pointer-events: none;
  }
  .panel > * { position: relative; z-index: 2; }

  .song-title { font-size: 11.5px; font-weight: 400; margin: 4px 0 6px 18px; }
  .body-copy { font-size: 8.3px; line-height: 15.3px; }
  .body-copy + .song-title { margin-top: 11px; }

  .thanks { text-align: center; margin-top: 76px; }
  .thanks-title { font-size: 12px; font-weight: 400; margin-bottom: 8px; }
  .thanks-list { list-style: none; font-size: 8.3px; line-height: 20px; }

  .dedication { padding-top: 4px; }
  .dedication .lead { font-size: 12px; font-weight: 400; margin: 4px 0 4px 14px; }
  .dedication p { font-size: 11.3px; line-height: 16.5px; margin-bottom: 4px; }

  .cover {
    position: absolute; left: 740px; top: 0; width: 370px; height: 369px;
  }
  .cover-photo {
    position: absolute; inset: 0;
    background:
      radial-gradient(ellipse at 38% 45%, #d9a98e 0%, #a87457 22%, transparent 45%),
      radial-gradient(ellipse at 85% 50%, #5a4634 0%, #3b2c20 40%, transparent 70%),
      linear-gradient(160deg, #2f4a25 0%, #6b7f3b 40%, #3f3524 100%);
  }
  .cover-name {
    position: absolute; left: 14px; top: 10px; width: 350px;
    font-family: "Great Vibes", cursive; font-weight: 400; font-size: 60px;
    line-height: 1.2;
    color: var(--pink); white-space: nowrap; z-index: 3;
  }
  .cover-year {
    position: absolute; left: 50px; top: 240px;
    font-family: "Great Vibes", cursive; font-weight: 400; font-size: 56px;
    line-height: 1;
    color: rgba(245,154,196,.6); z-index: 3;
  }
</style>
</head>
<body>
<main class="canvas">

  <section class="spread spread--outside">
    <article class="panel panel--1">
      <h2 class="song-title">"Keep a Light on for Me"</h2>
      <p class="body-copy">I heard this song for the first time and sang it 3 days later for my end of the year choir concert. My mom had been searching songs for me to sing and as soon as she introduced this song to me I fell in love with it. This song is typically meant to be sung about a romantic love but while performing this song I couldn't help but think of my grandparents and how they are always watching over me. I dedicate this song to my guardian angels, my protectors, and the two people that I love and miss more than anything in this world Oma and Opa.</p>
      <h2 class="song-title">"Lean On Us"</h2>
      <p class="body-copy">When I first sang this song I was performing at my voice recital for school. I chose to sing this song because it was fun and sweet. In the past few months this song has become very real to me. Although God and family are top priorities in my life, friends are such a huge part of my life as well. In 6Th grade I started a friendship with someone that I never knew would make such a great impact on my life. She became someone that I looked up to and someone that I could truly call my best friend. I dedicate</p>
    </article>

    <article class="panel panel--2">
      <p class="body-copy">this song to Kaylee Brandt for always putting up with me and investing in not only my life but my family's life. No matter where life takes us in the next year I will forever be thankful for her friendship.</p>
      <div class="thanks">
        <h2 class="thanks-title">Special thanks to:</h2>
        <ul class="thanks-list">
          <li>My Momma</li>
          <li>Marla Quince (voice coach)</li>
          <li>Lulu Padgett (High School choir director)</li>
          <li>Mark Ostrand</li>
          <li>Grant Vossler (Producer)</li>
        </ul>
      </div>
    </article>

    <div class="cover">
      <div class="cover-photo" role="img" aria-label="Portrait photograph of the singer leaning against a tree trunk in a sunlit park"></div>
      <h1 class="cover-name">Maren Dulack</h1>
      <p class="cover-year">2014</p>
    </div>

    <div class="floral" role="img" aria-label="Decorative border of pink and red flowers, butterflies and swirling vines"></div>
  </section>

  <section class="spread spread--inside">
    <article class="panel panel--1 dedication">
      <h2 class="lead">I dedicate this cd to my mom.</h2>
      <p>Even though I don't show it all the time, I appreciate her and the unconditional love she shows me. Through everything that I do I want to make her proud.</p>
      <p>Thank you for always having hope and faith in me and providing a life for me that I am so blessed to live. I love you more an more every day</p>
    </article>

    <article class="panel panel--2">
      <h2 class="song-title">"Evening Lantern"</h2>
      <p class="body-copy">As many people know, "Evening Lantern" has been our most requested song to sing. Growing up I had heard my dad sing this song with my aunt and I was so mesmerized by their performances and couldn't wait to one day sing this song with my dad. My dad and I have been singing together since I was 4 but this song sparked a different kind of relationship and musical connection with him. It was challenging at first and he pushed me to work hard and to push myself to discover vocal capabilities that I didn't know I had. I dedicate this song to my dad for always motivating me to be the best I can be not only musically but socially, academically and most of all spiritually. Dad, I love you more than words can say.</p>
      <h2 class="song-title">"Open Road"</h2>
      <p class="body-copy">I have never been a fan of country music let alone attempted to sing a country song but this song completely changed my perspective on it. My dad and I first sang this song at our Pastors retirement party celebrating he and his wife's 23 year long dedication to our church and to recognize his love for country music. They became apart of our family in many ways</p>
    </article>

    <article class="panel panel--3">
      <p class="body-copy">and I am so blessed to call them family. This song is dedicated to Pastor Glen and Faye Durbin for everything fron putting up with my grandparents to sharing every Easter with us. I miss them so much but I know that they will forever be apart of our family no matter where God places them.</p>
      <h2 class="song-title">"All That Your Mercy Holds"</h2>
      <p class="body-copy">When first introduced to this song I hated it. When having to choose a song to sing I always went with a ballad because that was my comfort zone. So when asked to sing a gospel song I was very overwhelmed. I never fully understood why people would say that they are "in love with music" or "music was their passion". I obviously enjoyed music but I had never felt that connection with it until the first time I performed this song. Every note, every word, every dynamic meant something to me and my passion for music was forever changed. I dedicate this song to Tamsin Holgreve for working with me hour upon hour to help me vocally improve and for teaching me that it's okay to step outside the box and to not just be comfortable all the time.</p>
    </article>

    <div class="floral" role="img" aria-label="Decorative border of pink and red flowers, butterflies and swirling vines"></div>
  </section>

</main>
</body>
</html>
```